letterhead design

can you create a letterhead using the logo you created and the following:

318 W Dunthorpe Elgin IL 60187
(p) 847-512-3971
(f) 847-438-1065
www.thekestrinlawgroup.example

Industry/Entity Type

Law

Requirements
Must have
• Use logo attached: must have address 318 W Dunthorpe Elgin IL 60187 phone 847-512-3971 fax 847-438-1065
Should not have
• Nothing other thank logo and address/phone/website

```html
<!DOCTYPE html>
<html lang="en">
<head>
<meta charset="utf-8">
<title>Kestrin Law Group — Letterhead</title>
<link rel="stylesheet" href="https://fonts.googleapis.com/css2?family=Gilda+Display&display=swap">
<style>
  :root {
    --paper: #ffffff;
    --gold: #e0b45a;
    --gold-faint: #fbf1e2;
    --ink: #1f1f24;
  }
  * { box-sizing: border-box; margin: 0; padding: 0; }
  html, body {
    width: 921px;
    height: 1200px;
    overflow: hidden;
    background: var(--paper);
  }
  .letterhead {
    position: relative;
    width: 921px;
    height: 1200px;
    background: var(--paper);
  }
  .brand {
    position: absolute;
    top: 32px;
    left: 0;
    width: 100%;
    display: flex;
    flex-direction: column;
    align-items: center;
  }
  .brand-circle {
    width: 86px;
    height: 86px;
    border: 2px solid var(--gold);
    border-radius: 50%;
  }
  .brand-name {
    margin-top: 16px;
    font-family: "Gilda Display", serif;
    font-weight: 400;
    font-size: 24px;
    letter-spacing: 1px;
    line-height: 1;
    color: var(--gold);
  }
  .faint-circle {
    position: absolute;
    left: 61px;
    top: 969px;
    width: 230px;
    height: 230px;
    border: 6px solid var(--gold-faint);
    border-radius: 50%;
  }
  .contact {
    position: absolute;
    right: 32px;
    top: 1014px;
    list-style: none;
    font-family: "Gilda Display", serif;
    color: var(--ink);
    font-size: 15px;
  }
  .contact li {
    display: flex;
    align-items: center;
    justify-content: flex-end;
    gap: 12px;
    height: 35px;
  }
  .contact svg {
    width: 22px;
    height: 22px;
    fill: none;
    stroke: var(--gold);
    stroke-width: 1.3;
    stroke-linecap: round;
    stroke-linejoin: round;
  }
</style>
</head>
<body>
<main class="letterhead">
  <header class="brand">
    <div class="brand-circle" aria-hidden="true"></div>
    <div class="brand-name">Kestrin Law Group</div>
  </header>

  <div class="faint-circle" aria-hidden="true"></div>

  <ul class="contact">
    <li>318 W Dunthorpe Elgin IL 60187
      <svg viewBox="0 0 24 24" aria-label="Address"><path d="M12 17s-5-5.2-5-9a5 5 0 0 1 10 0c0 3.8-5 9-5 9z"/><circle cx="12" cy="8" r="2"/><path d="M8 16.5c-2.5.5-4 1.4-4 2.5 0 1.7 3.6 3 8 3s8-1.3 8-3c0-1.1-1.5-2-4-2.5"/></svg>
    </li>
    <li>847-512-3971
      <svg viewBox="0 0 24 24" aria-label="Phone"><path d="M5 3l3 .5 1.5 4-2 1.5a11 11 0 0 0 7.5 7.5l1.5-2 4 1.5.5 3c-.5 1.5-2 2-3.5 2C10 21 3 14 3 6.5 3 5 3.5 3.5 5 3z"/><path d="M14 3a7 7 0 0 1 7 7M14 6.5a3.5 3.5 0 0 1 3.5 3.5"/></svg>
    </li>
    <li>847-438-1065
      <svg viewBox="0 0 24 24" aria-label="Fax"><path d="M7 11V2h8l3 3v6"/><path d="M15 2v3h3"/><rect x="3" y="11" width="18" height="8" rx="1"/><path d="M6 19v3h12v-3M7 15h10"/></svg>
    </li>
    <li>www.thekestrinlawgroup.example
      <svg viewBox="0 0 24 24" aria-label="Website"><circle cx="12" cy="12" r="9.5"/><ellipse cx="12" cy="12" rx="4" ry="9.5"/><path d="M2.5 12h19M4 7h16M4 17h16"/></svg>
    </li>
  </ul>
</main>
</body>
</html>
```